Upgrade my Web to PHP format

I need move my web site http://qrnlivo7.example to PHP format my hosting is running under Linux with MySQL , all information is on old Web site and we need move to the new Web Design , We would like to see designs that use the color of our logo.

The final design should communicate about security software , security services and hosting Vorlan Stride k server.

Is very important easy installation and instructions of installation.

Target Market(s)

Bank and security company

Industry/Entity Type

Computer Security

Number of Pages Required

5+ page

Font styles to use
Sans Serif
Other font styles liked:
• arial, verdana.

Colors
3276b5
33a6d7
85cae6
85acd3
88d0c7

Requirements
Must have
• respect to our colors and all link to all pages, videos , and PDF.
Nice to have
• I would like design about security server and services , developer software security.
Should not have
• Anti Virus

```html
<!DOCTYPE html>
<html lang="en">
<head>
<meta charset="utf-8">
<title>Kelvaro Support</title>
<link rel="stylesheet" href="https://fonts.googleapis.com/css2?family=Roboto:wght@300;400;500&display=swap">
<style>
:root{
  --blue:#3276b5;
  --sky:#33a6d7;
  --pale:#85cae6;
  --steel:#85acd3;
  --teal:#88d0c7;
  --ink:#333;
  --muted:#555;
  --white:#fff;
}
*{margin:0;padding:0;box-sizing:border-box}
html,body{width:698px;height:1200px;overflow:hidden;background:#fff}
body{position:relative;font-family:"Roboto",Arial,sans-serif;color:var(--ink)}
h1,h2{font-weight:400}
.abs{position:absolute}
/* header */
.site-header{left:0;top:0;width:698px;height:74px;background:#fff}
.brand{left:44px;top:22px;display:flex;align-items:center;gap:6px}
.brand-dot{width:30px;height:30px;border-radius:50%;background:var(--blue)}
.brand-name{font-size:12px;font-weight:500;color:var(--blue);letter-spacing:.5px}
.main-nav{left:205px;top:29px;display:flex;align-items:center;font-size:7.4px;font-weight:500;color:#222;text-transform:uppercase}
.main-nav span{padding:0 12.4px;line-height:22px}
.main-nav .current{background:var(--sky);color:#fff;padding:0 11px}
/* hero */
.hero{left:0;top:74px;width:698px;height:234px;background:linear-gradient(90deg,#5d7790 0%,#8aa3b8 40%,#c3ccd3 70%,#a7b6c4 100%)}
.hero-title{left:44px;top:160px;font-size:25.5px;color:#fff;line-height:32px;letter-spacing:.5px}
.hero-title span{display:inline-block;background:rgba(50,118,181,.85);padding:0 6px;margin-bottom:1px}
.slide-arrows{left:44px;top:268px;display:flex;gap:5px}
.slide-arrows svg{width:17px;height:17px}
/* sections */
.section-title{font-size:13px;color:var(--blue);text-transform:uppercase}
.body-text{font-size:7.4px;line-height:14.4px;color:#444}
.btn{display:inline-block;background:var(--steel);color:#fff;font-size:7px;font-weight:500;text-transform:uppercase;text-align:center;line-height:20px;height:20px}
.welcome-title{left:44px;top:332px}
.welcome-text{left:44px;top:352px;width:610px}
.welcome-btn{left:44px;top:408px;width:61px}
/* offers */
.offers{left:0;top:449px;width:446px;height:226px;background:var(--teal)}
.offers-title{left:0;top:473px;width:476px;text-align:center;font-size:13px;color:#fff;text-transform:uppercase}
.offer{top:505px;width:130px;text-align:center}
.offer-icon{width:47px;height:47px;border-radius:50%;background:var(--blue);margin:0 auto;display:flex;align-items:center;justify-content:center}
.offer-name{margin-top:12px;font-size:9.5px;color:var(--blue);text-transform:uppercase}
.offer-text{margin:4px auto 0;width:122px;font-size:7.2px;line-height:12.3px;color:#555}
.offer .btn{margin-top:16px;width:62px}
.video-panel{left:446px;top:449px;width:252px;height:226px;background:linear-gradient(135deg,#4a4d52,#2d3034 60%,#55595e)}
.video-title{left:446px;top:501px;width:252px;text-align:center;font-size:12.5px;line-height:18px;color:#fff;text-transform:uppercase}
.play{left:538px;top:547px}
.video-btn{left:504px;top:607px;width:105px;height:25px;line-height:25px;background:var(--blue);font-size:8px}
/* principles */
.principles-title{left:43px;top:699px}
.principles-text{left:44px;top:724px;width:332px}
.principles-text p{margin-bottom:3px}
.principles-btn{left:44px;top:849px;width:61px}
.word-cloud{left:395px;top:715px;width:262px;height:155px;background:linear-gradient(135deg,#e6eaee,#c9d6e3)}
/* clients */
.divider{left:0;top:892px;width:698px;height:1px;background:#e3e3e3}
.clients-title{left:43px;top:907px}
.clients-arrows{left:632px;top:909px;display:flex;gap:4px}
.client{top:938px;width:114px;height:41px;border:1px solid #ddd;display:flex;align-items:center;justify-content:center;font-size:11px;font-weight:500;color:var(--blue)}
/* map & contact */
.map{left:0;top:997px;width:698px;height:143px;background:linear-gradient(180deg,#d9d6d0,#cfcbc4)}
.contact-card{left:44px;top:1026px;width:181px;height:87px;background:#fff;padding:8px 10px;font-style:normal}
.contact-card h2{font-size:13px;color:var(--blue);text-transform:uppercase;margin-bottom:5px}
.contact-card p{font-size:7.2px;line-height:12.3px;color:#333}
.contact-card .link{color:var(--blue);display:flex;align-items:center;gap:3px}
/* footer */
.site-footer{left:0;top:1140px;width:698px;height:60px;background:var(--sky)}
.footer-mark{left:44px;top:1156px;width:30px;height:30px;border-radius:50%;background:#fff}
.legal{left:94px;top:1159px;font-size:6.8px;line-height:11.5px;color:#fff}
.connect{left:418px;top:1165px;font-size:7.5px;color:#fff;display:flex;align-items:center;gap:6px;text-transform:uppercase}
.connect i{display:inline-block;width:9px;height:9px;border-radius:50%;background:#fff}
.trust-badge{left:568px;top:1154px;width:86px;height:34px;border-radius:17px;background:#fff}
</style>
</head>
<body>

<header class="site-header abs">
  <div class="brand abs"><span class="brand-dot"></span><span class="brand-name">KELVARO SUPPORT</span></div>
  <nav class="main-nav abs">
    <span class="current">Home</span><span>About</span><span>Products</span><span>Services</span><span>Cloud Services</span><span>Support Tickets</span><span>Contact Us</span>
  </nav>
</header>

<section class="hero abs" role="img" aria-label="Photo of a smiling professional in a bright office"></section>
<h1 class="hero-title abs"><span>THE IDEAL PROFESSIONAL IT</span><br><span>SERVICES &amp; SUPPORT.</span></h1>
<div class="slide-arrows abs">
  <svg viewBox="0 0 20 20"><circle cx="10" cy="10" r="10" fill="#333" opacity=".8"/><path d="M12 5 7 10l5 5" stroke="#fff" stroke-width="2" fill="none"/></svg>
  <svg viewBox="0 0 20 20"><circle cx="10" cy="10" r="10" fill="#333" opacity=".8"/><path d="M8 5l5 5-5 5" stroke="#fff" stroke-width="2" fill="none"/></svg>
</div>

<h2 class="section-title welcome-title abs">Welcome to our website</h2>
<p class="body-text welcome-text abs">Aliquam molestie, mi et imperdiet euismod, dui purus auctor tellus, et interdum lacus lectus et ante. Sed accumsan sollicitudin sapien, sit amet adipiscing turpis gravida ac. In congue, neque ac lobortis volutpat, libero mauris varius mi, vitae suscipit ipsum ligula vitae risus. Duis aliquam nibh a dui iaculis viverra id a velit. Vivamus egestas risus in magna varius commodo. Sed semper viverra egestas. Etiam pretium porttitor lectus, vel ornare neque porta volutpat.</p>
<a class="btn welcome-btn abs">Read more</a>

<section class="offers abs"></section>
<h2 class="offers-title abs">What we offers</h2>
<div class="offer abs" style="left:38px">
  <div class="offer-icon"><svg width="22" height="22" viewBox="0 0 24 24" fill="#fff"><circle cx="12" cy="10" r="5.5"/><rect x="9.5" y="15" width="5" height="4" rx="1"/><path d="M12 1v2M4 4l1.5 1.5M20 4l-1.5 1.5M1 11h2M21 11h2" stroke="#fff" stroke-width="1.5"/></svg></div>
  <div class="offer-name">All about IT</div>
  <div class="offer-text">Duis aliquam nibh a dui iaculis viverra id a velit. Vivamus egestas risus in magna varius..</div>
  <a class="btn">Read more</a>
</div>
<div class="offer abs" style="left:172px">
  <div class="offer-icon"><svg width="22" height="22" viewBox="0 0 24 24"><circle cx="9" cy="13" r="5" fill="none" stroke="#fff" stroke-width="3" stroke-dasharray="2.5 1.5"/><circle cx="9" cy="13" r="2" fill="#fff"/><path d="M14 9l7-6" stroke="#fff" stroke-width="2.5"/></svg></div>
  <div class="offer-name">Integrated services</div>
  <div class="offer-text">Duis aliquam nibh a dui iaculis viverra id a velit. Vivamus egestas risus in magna varius..</div>
  <a class="btn">Read more</a>
</div>
<div class="offer abs" style="left:306px">
  <div class="offer-icon"><svg width="22" height="22" viewBox="0 0 24 24" fill="#fff"><circle cx="12" cy="9" r="5"/><path d="M3 22c0-5 4-7 9-7s9 2 9 7z"/><path d="M5 10a7 7 0 0 1 14 0" stroke="#fff" stroke-width="1.5" fill="none"/></svg></div>
  <div class="offer-name">Customer service</div>
  <div class="offer-text">Duis aliquam nibh a dui iaculis viverra id a velit. Vivamus egestas risus in magna varius..</div>
  <a class="btn">Read more</a>
</div>

<section class="video-panel abs" role="img" aria-label="Photo of two technicians shaking hands beside a server rack"></section>
<h2 class="video-title abs">The ideal professional IT<br>services &amp; support.</h2>
<svg class="play abs" width="38" height="38" viewBox="0 0 38 38"><circle cx="19" cy="19" r="18" fill="#fff"/><path d="M15 11l12 8-12 8z" fill="#222"/></svg>
<a class="btn video-btn abs">Watch a video</a>

<h2 class="section-title principles-title abs">Effective operating principles</h2>
<div class="body-text principles-text abs">
  <p>We are a company with extensive experience in the area of information technology for environments Vorlan Stride k (VS/410), and we are part of the ISV Business Partners.</p>
  <p>Our strength lies in the extensive knowledge and experience in the area of computer security and support in providing the best solutions, which cover the requirements of confidentiality and availability of data on that platform.</p>
  <p>As a result of this experience, we developed the product IP Security to ensure that monitoring and access control to the Vorlan Stride k.</p>
</div>
<a class="btn principles-btn abs">Read more</a>
<div class="word-cloud abs" role="img" aria-label="Word cloud illustration of technology, software, network and database terms"></div>

<div class="divider abs"></div>
<h2 class="section-title clients-title abs">Our clients</h2>
<div class="clients-arrows abs">
  <svg width="10" height="12" viewBox="0 0 10 12"><path d="M7 1 2 6l5 5" stroke="#444" stroke-width="2" fill="none"/></svg>
  <svg width="10" height="12" viewBox="0 0 10 12"><path d="M3 1l5 5-5 5" stroke="#444" stroke-width="2" fill="none"/></svg>
</div>
<div class="client abs" style="left:44px">Norvatek</div>
<div class="client abs" style="left:168px">Pellan Bank</div>
<div class="client abs" style="left:292px">Bancorial</div>
<div class="client abs" style="left:416px">Tresmar Bank</div>
<div class="client abs" style="left:541px">Veluno</div>

<section class="map abs" role="img" aria-label="Street map showing the office location"></section>
<address class="contact-card abs">
  <h2>Contact info</h2>
  <p>4120 Calder Avenue Suite 210<br>Harbor City, FL, 30412</p>
  <p class="link" style="margin-top:3px">
    <svg width="7" height="7" viewBox="0 0 10 10"><path d="M2 1l2 2-1 1.5 2.5 2.5L7 6l2 2-1.5 1.5C5 9.5.5 5 .5 2.5z" fill="#3276b5"/></svg>+1 (555) 0142290 &nbsp;|&nbsp;
    <svg width="7" height="7" viewBox="0 0 10 10"><rect x="1" y="3" width="8" height="6" fill="#3276b5"/><rect x="3" y="1" width="4" height="3" fill="#3276b5"/></svg>+1 (555) 0142290
  </p>
  <p class="link"><svg width="7" height="6" viewBox="0 0 10 8"><rect width="10" height="8" fill="#3276b5"/><path d="M0 0l5 4 5-4" stroke="#fff" fill="none"/></svg>contact@kelvarosupport.example</p>
</address>

<footer class="site-footer abs"></footer>
<div class="footer-mark abs"></div>
<p class="legal abs">Copyright © 2015. Company Name All Right Reserved<br>Terms of Services &nbsp;|&nbsp; Privacy Policy</p>
<div class="connect abs">Connect us <i></i><i></i><i></i><i></i></div>
<div class="trust-badge abs" role="img" aria-label="Security certificate badge"></div>

</body>
</html>
```